Business Card Design for Event Planning Company

Create a business card for event planning company using our new logo. After I pick the design, I will need files made for 6 employees. Our company provides event design & logistics services as well as venue management. The font should be sans serif and complementary to the logo. I will need to know the name of the font selected for the final design. The phone numbers listed should be separated by "." not "-"

Address for the card
PO Box 318, Washington, DC 20019

Card One
Lorna Pettibone
lpettibone@galavoyant.com
202.481.7730

Card Two
Miriam Okonkwo
mokonkwo@galavoyant.com
202.556.2047

Card Three
Tessa Varnholt
tvarnholt@galavoyant.com
978.620.4471

Card Four
Robin Fess
rfess@galavoyant.com
202.718.3362

Card Five
Ada-Rose Pelletan-Uzor
adarose@galavoyant.com
202.839.1205

Card Six
Beatrix Holloway
Beatrix@galavoyant.com
202.492.6618

Target Market(s)

Corporate/Non-Profit

Industry/Entity Type

Event Planning

Contact Information for Business Card

Address for the card

Card One
Lorna Pettibone
lpettibone@galavoyant.com
202.481.7730

Card Two
Miriam Okonkwo
202.556.2047

Card Three
Tessa Varnholt
978.620.4471

Card Four
Robin Fess
rfess@galavoyant.com
202.718.3362

Card Five
Ada-Rose Pelletan-Uzor
202.839.1205

Card Six
Beatrix Holloway
202.492.6618

Font styles to use
Sans Serif

Colors

Designer to choose colors to be used in the design.

Requirements
Must have
• Two-sided with logo
Should not have
• Extra colors or be too busy

```html
<!DOCTYPE html>
<html lang="en">
<head>
<meta charset="utf-8">
<title>Galavoyant Business Card</title>
<link href="https://fonts.googleapis.com/css2?family=Questrial&family=Lato:wght@400;700&display=swap" rel="stylesheet">
<style>
  :root {
    --teal: #5ba9a8;
    --ink: #231f20;
    --card-dark: #262223;
    --paper: #ffffff;
    --stage: #e9eaea;
    --rule: #b9b9b9;
  }
  * { box-sizing: border-box; margin: 0; padding: 0; }
  html, body { width: 1200px; height: 1200px; overflow: hidden; background: var(--stage); }
  .canvas { position: relative; width: 1200px; height: 1200px; }

  .card {
    position: absolute;
    left: 150px;
    width: 900px;
    height: 514px;
    overflow: hidden;
    box-shadow: 0 6px 18px rgba(0,0,0,0.12);
  }
  .card-back { top: 56px; background: var(--card-dark); }
  .card-front { top: 630px; background: var(--paper); }

  .wordmark {
    font-family: "Questrial", sans-serif;
    font-weight: 400;
    letter-spacing: 1px;
    display: flex;
    align-items: center;
    justify-content: center;
    gap: 18px;
  }
  .wordmark-dot { border-radius: 50%; background: var(--teal); flex: none; }

  .card-back .wordmark {
    position: absolute; inset: 0;
    color: var(--paper);
    font-size: 64px;
  }
  .card-back .wordmark-dot { width: 34px; height: 34px; }

  .card-front .wordmark {
    position: absolute; left: 0; right: 0; top: 150px;
    color: var(--ink);
    font-size: 92px;
  }
  .card-front .wordmark-dot { width: 44px; height: 44px; }

  .contact-row {
    position: absolute; left: 0; right: 0; top: 348px;
    display: flex; align-items: flex-start;
    padding: 0 40px;
  }
  .holder-name {
    font-family: "Questrial", sans-serif;
    font-size: 25px;
    color: var(--ink);
    width: 270px;
    padding-top: 6px;
  }
  .holder-name .surname { color: var(--teal); }
  .divider { width: 1.5px; height: 62px; background: var(--rule); margin: 0 22px; flex: none; }
  .address, .contact-list {
    font-family: "Lato", sans-serif;
    font-size: 19px;
    color: var(--ink);
    line-height: 1.45;
  }
  .address { width: 260px; }
  .contact-list { list-style: none; padding-top: 4px; }
  .contact-list li { display: flex; align-items: center; gap: 12px; }
  .contact-icon {
    width: 24px; height: 24px; border-radius: 50%;
    background: var(--teal);
    display: flex; align-items: center; justify-content: center; flex: none;
  }

  .accent-bar {
    position: absolute; left: 0; right: 0; top: 462px; height: 12px;
    display: flex;
  }
  .accent-bar .teal { width: 52%; background: var(--teal); }
  .accent-bar .dark { flex: 1; background: var(--ink); }
</style>
</head>
<body>
<main class="canvas">
  <section class="card card-back" aria-label="Card back">
    <div class="wordmark"><span class="wordmark-dot"></span><span>galavoyant</span></div>
  </section>

  <section class="card card-front" aria-label="Card front">
    <div class="wordmark"><span class="wordmark-dot"></span><span>galavoyant</span></div>

    <div class="contact-row">
      <p class="holder-name">Lorna <span class="surname">Pettibone</span></p>
      <span class="divider"></span>
      <p class="address">PO Box 318, Washington<br>DC 20019</p>
      <span class="divider"></span>
      <ul class="contact-list">
        <li>
          <span class="contact-icon">
            <svg width="14" height="14" viewBox="0 0 24 24" aria-hidden="true"><path fill="#fff" d="M6.6 10.8a15.1 15.1 0 0 0 6.6 6.6l2.2-2.2a1 1 0 0 1 1-.25 11.4 11.4 0 0 0 3.6.57 1 1 0 0 1 1 1V20a1 1 0 0 1-1 1A17 17 0 0 1 3 4a1 1 0 0 1 1-1h3.5a1 1 0 0 1 1 1c0 1.25.2 2.45.57 3.57a1 1 0 0 1-.25 1z"/></svg>
          </span>
          202.481.7730
        </li>
        <li>
          <span class="contact-icon">
            <svg width="14" height="14" viewBox="0 0 24 24" aria-hidden="true"><rect x="3" y="6" width="18" height="12" rx="1" fill="none" stroke="#fff" stroke-width="2"/><path d="M3 7l9 6 9-6" fill="none" stroke="#fff" stroke-width="2"/></svg>
          </span>
          lpettibone@galavoyant.com
        </li>
      </ul>
    </div>

    <div class="accent-bar"><span class="teal"></span><span class="dark"></span></div>
  </section>
</main>
</body>
</html>
```